Business Card/Letterhead for Construction Company
Ronald Pike Construction
Professional
Ronald P. Pike
5702 Meadowlark Court, Suite #4
Brookhaven, TN 38115
ronald@ronaldpikeconstruction.example
www.ronaldpikeconstruction.example
Possibly add Facebook page:
www.friendpages.example/pikehouses
Navy Logo
Main Logo

```html
<!DOCTYPE html>
<html lang="en">
<head>
<meta charset="utf-8">
<title>Ronald Pike Construction – Business Card</title>
<link rel="stylesheet" href="https://fonts.googleapis.com/css2?family=Cinzel:wght@400;600&display=swap">
<style>
  :root {
    --navy: #1c3564;
    --ink: #2b3a55;
    --grey: #5d6470;
    --rule: #9aa3b2;
    --paper: #ffffff;
    --paper-shade: #eef0f3;
    --backdrop: #e6e8ec;
  }
  * { box-sizing: border-box; margin: 0; padding: 0; }
  html, body {
    width: 1200px; height: 914px; overflow: hidden;
    background: var(--backdrop);
  }
  .stage {
    width: 1200px; height: 914px;
    display: flex; align-items: center; justify-content: center;
  }
  .card {
    width: 1000px; height: 572px;
    background: var(--navy);
    padding: 30px;
    box-shadow: 0 18px 40px rgba(20, 30, 50, 0.25);
  }
  .card-face {
    position: relative;
    width: 100%; height: 100%;
    background: radial-gradient(ellipse at 45% 40%, var(--paper) 55%, var(--paper-shade) 100%);
    font-family: "Cinzel", Georgia, serif;
    color: var(--ink);
  }
  .brand {
    position: absolute; left: 190px; top: 100px;
    display: flex; align-items: center;
  }
  .brand-mark {
    width: 110px; height: 110px;
    background: var(--navy);
  }
  .brand-divider {
    width: 2px; height: 120px;
    background: var(--rule);
    margin: 0 22px;
  }
  .brand-name {
    color: var(--navy);
    font-weight: 600;
    line-height: 1;
  }
  .brand-name .primary { display: block; font-size: 56px; letter-spacing: 1px; }
  .brand-name .secondary { display: block; font-size: 26px; letter-spacing: 9px; margin-top: 8px; text-align: right; }
  .details {
    position: absolute; left: 0; right: 0; top: 300px;
    display: flex; justify-content: center;
  }
  .person {
    width: 330px; text-align: right; padding-right: 22px;
  }
  .person-name {
    font-size: 26px; font-weight: 600; color: var(--navy);
    margin-bottom: 18px;
  }
  .person-address {
    font-size: 16px; color: var(--grey); line-height: 1.65;
  }
  .details-divider {
    width: 2px; height: 130px; background: var(--rule); margin-top: 50px;
  }
  .contact-list {
    list-style: none; padding-left: 18px; margin-top: 48px;
  }
  .contact-item {
    display: flex; align-items: center;
    font-size: 15px; color: var(--grey);
    height: 29px;
    white-space: nowrap;
  }
  .contact-item.phone { font-size: 21px; color: var(--ink); height: 31px; }
  .contact-icon {
    width: 19px; height: 19px; margin-right: 10px; flex: none;
  }
</style>
</head>
<body>
<main class="stage">
  <article class="card">
    <div class="card-face">
      <header class="brand">
        <div class="brand-mark"></div>
        <div class="brand-divider"></div>
        <div class="brand-name">
          <span class="primary">RONALD PIKE</span>
          <span class="secondary">CONSTRUCTION</span>
        </div>
      </header>

      <section class="details">
        <div class="person">
          <p class="person-name">Ronald P. Pike</p>
          <p class="person-address">5702 Meadowlark Court, Suite #4<br>Brookhaven, TN 38115</p>
        </div>
        <div class="details-divider"></div>
        <ul class="contact-list">
          <li class="contact-item phone">
            <svg class="contact-icon" viewBox="0 0 20 20"><circle cx="10" cy="10" r="10" fill="#1c3564"/><path d="M7 5l2 2-1 1.5c.6 1.4 1.6 2.4 3 3L12.5 10l2 2-1.3 1.8C9.5 13.5 6.5 10.5 6 6.6z" fill="#fff"/></svg>
            901-555-0162
          </li>
          <li class="contact-item phone">
            <svg class="contact-icon" viewBox="0 0 20 20"><circle cx="10" cy="10" r="10" fill="#1c3564"/><path d="M7 5l2 2-1 1.5c.6 1.4 1.6 2.4 3 3L12.5 10l2 2-1.3 1.8C9.5 13.5 6.5 10.5 6 6.6z" fill="#fff"/></svg>
            901-555-0124
          </li>
          <li class="contact-item">
            <svg class="contact-icon" viewBox="0 0 20 20"><circle cx="10" cy="10" r="10" fill="#1c3564"/><rect x="5" y="6.5" width="10" height="7" fill="none" stroke="#fff" stroke-width="1.2"/><path d="M5 6.5l5 4 5-4" fill="none" stroke="#fff" stroke-width="1.2"/></svg>
            ronald@ronaldpikeconstruction.example
          </li>
          <li class="contact-item">
            <svg class="contact-icon" viewBox="0 0 20 20"><circle cx="10" cy="10" r="10" fill="#1c3564"/><circle cx="10" cy="10" r="5" fill="none" stroke="#fff" stroke-width="1.2"/><path d="M5 10h10M10 5c-2.5 3-2.5 7 0 10M10 5c2.5 3 2.5 7 0 10" fill="none" stroke="#fff" stroke-width="1"/></svg>
            www.ronaldpikeconstruction.example
          </li>
        </ul>
      </section>
    </div>
  </article>
</main>
</body>
</html>
```